Company folder for engineering company in packaging sector

I look for design a flyer of 6 front pages folded . When you open the 3rd page is the center one (behind the 6th one), the first and second on the left and the forth, fifth on the right.
So I open the first page fro tight to left, then left to right.
The third page must be emotional because when you open the folder is the central one.
I add file movie to show an example of folder
Please check the power point trial.

I add acad lay out to if needed to add .

Target Market(s)

We project and manufacture packaging line (please check the power point file attached

Industry/Entity Type

It Company

Requirements
Must have
• The Logo is already in the file if is needed other images or in vectorial format please specify
Nice to have
• It's possible to add a pocket for adding document (as offer) and space for business card

```html
<!DOCTYPE html>
<html lang="en">
<head>
<meta charset="utf-8">
<title>Nortec Group – Folder Inside Spread</title>
<link href="https://fonts.googleapis.com/css2?family=Arimo:ital,wght@0,400;0,700;1,700&display=swap" rel="stylesheet">
<style>
  :root {
    --blue: #1f6cb5;
    --blue-dark: #1a5ea3;
    --green: #2eb872;
    --orange: #f7941d;
    --sky: #17a7e0;
    --panel-grey: #ececec;
    --header-grey: #efefef;
    --text: #2b2b2b;
    --muted: #555;
    --rule: #b5b5b5;
  }
  * { margin: 0; padding: 0; box-sizing: border-box; }
  html, body { width: 1200px; height: 566px; overflow: hidden; background: #fff; }
  body { font-family: "Arimo", Arial, sans-serif; color: var(--text); }
  .spread { position: relative; width: 1200px; height: 566px; overflow: hidden; background: #fff; }
  .backdrop { position: absolute; left: 0; top: 0; }
  .abs { position: absolute; }

  /* Engineering panel */
  .section-pill {
    left: 0; top: 21px; height: 22px; width: 122px;
    background: var(--blue); color: #fff; font-size: 16px;
    line-height: 22px; padding-left: 24px; border-radius: 0 11px 11px 0;
  }
  .eng-copy { left: 25px; width: 360px; color: var(--blue); font-size: 10.6px; line-height: 13px; }
  .eng-copy.p1 { top: 55px; }
  .eng-copy.p2 { top: 107px; }
  .cycle, .steps { position: absolute; left: 0; top: 0; }
  .step-label { color: #fff; font-size: 10.6px; line-height: 12.5px; }

  /* Customer service panel */
  .service-title { left: 486px; top: 34px; font-size: 16px; font-weight: 400; color: #222; display: flex; align-items: center; }
  .service-title .initial {
    width: 20px; height: 20px; border-radius: 50%; background: var(--blue); color: #fff;
    font-size: 15px; line-height: 20px; text-align: center; margin-right: 1px;
  }
  .body-copy { font-size: 10.6px; line-height: 13px; color: var(--text); }
  .intro { left: 470px; top: 89px; width: 295px; }
  .spares { left: 466px; top: 122px; }
  .bullets { left: 503px; list-style: none; }
  .bullets li { position: absolute; left: 0; white-space: nowrap; padding-left: 9px; }
  .bullets li::before {
    content: ""; position: absolute; left: 0; top: 4px; width: 5px; height: 5px;
    border-radius: 50%; background: var(--blue);
  }
  .sub-head {
    left: 433px; width: 191px; color: var(--blue); font-weight: 700; font-style: italic;
    font-size: 11.5px; border-bottom: 1.5px solid var(--blue); padding-bottom: 1px;
  }
  .sub-copy { left: 433px; width: 345px; }
  .contact { top: 412px; width: 200px; }
  .contact .brand { color: var(--blue); font-size: 18px; font-weight: 700; display: flex; align-items: center; gap: 5px; height: 26px; white-space: nowrap; }
  .contact .brand i { width: 9px; height: 9px; background: var(--blue); display: inline-block; }
  .contact .name { margin-top: 17px; color: var(--blue); font-weight: 700; font-size: 11px; line-height: 13px; }
  .contact .line { font-size: 10.6px; line-height: 13px; color: var(--muted); white-space: nowrap; }
  .contact .phone { margin-top: 6px; }
  .contact b { color: var(--blue); }
  .contact .email { padding-left: 4px; }
  .contact-left { left: 411px; }
  .contact-right { left: 649px; }
  .divider { left: 631px; top: 419px; width: 1.5px; height: 110px; background: var(--blue); }
  .web { left: 523px; top: 541px; color: var(--blue); font-size: 14px; }

  /* Cover photo panel */
  .cover-photo {
    left: 800px; top: 0; width: 400px; height: 566px;
    background:
      radial-gradient(ellipse at 30% 30%, rgba(80,140,70,0.35), transparent 45%),
      radial-gradient(ellipse at 70% 80%, rgba(255,255,255,0.55), transparent 55%),
      linear-gradient(160deg, #d9dcdd 0%, #9aa0a3 30%, #c9cdcf 55%, #7d8386 75%, #d5d8da 100%);
  }
  .cover-badge {
    left: 858px; top: 227px; width: 281px; height: 110px;
    background: #fff; border: 5px solid var(--blue-dark); border-radius: 8px;
    display: flex; align-items: center; justify-content: center; gap: 10px;
  }
  .cover-badge span { color: var(--blue-dark); font-size: 31px; font-weight: 700; white-space: nowrap; }
  .cover-badge i { width: 14px; height: 14px; background: var(--blue-dark); display: inline-block; }
</style>
</head>
<body>
<main class="spread">

  <svg class="backdrop" width="1200" height="566" viewBox="0 0 1200 566" aria-hidden="true">
    <polygon points="0,0 482,0 326,566 0,566" fill="var(--panel-grey)"/>
    <polygon points="482,0 800,0 800,76 461,76" fill="var(--header-grey)"/>
    <polygon points="476,0 488,0 466,76 454,76" fill="var(--blue)"/>
    <line x1="398" y1="0" x2="398" y2="566" stroke="var(--rule)" stroke-width="1" stroke-dasharray="8 7"/>
  </svg>

  <!-- Engineering -->
  <div class="abs section-pill">Engineering</div>
  <p class="abs eng-copy p1">Our team will work closely with customer operations people, providing the highest professionalism and competence, from the feasibility analysis up to the final project definition.</p>
  <p class="abs eng-copy p2">Our network of specialized engineers, with a solid experience and expert knowledge of each specific machine, is at your disposal to provide all the assistance you may require and meet your specific needs.</p>

  <svg class="cycle" width="400" height="566" viewBox="0 0 400 566" role="img" aria-label="Cycle of scope, cost and time around quality packaging">
    <g fill="none" stroke-width="34">
      <path d="M137.8 209.7 A65 65 0 0 1 232.8 197.2" stroke="var(--green)"/>
      <path d="M252.1 224.8 A65 65 0 0 1 213.2 308.1" stroke="var(--orange)"/>
      <path d="M179.7 311 A65 65 0 0 1 127 235.7" stroke="var(--sky)"/>
    </g>
    <polygon points="248.2,178.8 217.4,215.6 247.3,214.5" fill="var(--green)"/>
    <polygon points="221.4,330.6 205,285.5 191,312" fill="var(--orange)"/>
    <polygon points="103.3,231.5 150.6,239.9 134.7,214.5" fill="var(--sky)"/>
    <g fill="#fff" font-family="Arimo, Arial, sans-serif" font-size="17">
      <text x="185" y="193" text-anchor="middle" transform="rotate(8 185 188)">Scope</text>
      <text x="246" y="272" text-anchor="middle" transform="rotate(70 246 268)">Cost</text>
      <text x="137" y="280" text-anchor="middle" transform="rotate(-70 137 275)">Time</text>
    </g>
    <g fill="var(--blue)" font-family="Arimo, Arial, sans-serif" font-size="14" text-anchor="middle">
      <text x="191" y="237">Quatliy</text>
      <text x="191" y="255">Packaging</text>
    </g>
  </svg>

  <svg class="steps" width="400" height="566" viewBox="0 0 400 566" aria-hidden="true">
    <g fill="var(--blue)">
      <polygon points="14,339 62,339 82,381 62,424 14,424"/>
      <polygon points="66,339 145,339 165,381 145,424 66,424 86,381"/>
      <polygon points="149,339 238,339 258,381 238,424 149,424 169,381"/>
      <polygon points="242,339 345,339 365,381 345,424 242,424 262,381"/>
    </g>
  </svg>
  <div class="abs step-label" style="left:23px;top:369px;">Project<br>Analysis</div>
  <div class="abs step-label" style="left:89px;top:362px;">Project<br>Definition<br>&amp; Planning</div>
  <div class="abs step-label" style="left:170px;top:369px;">Project<br>Implementation</div>
  <div class="abs step-label" style="left:267px;top:355px;">Project<br>Commissioning,<br>Start up &amp;<br>PerformanceTest</div>

  <!-- Customer Service -->
  <h2 class="abs service-title"><span class="initial">C</span>ustomer Service</h2>
  <p class="abs body-copy intro">We offer all our knowledge and expertise in order to improve line performance.</p>
  <p class="abs body-copy spares">Spare parts &amp; Upgrades</p>
  <ul class="abs body-copy bullets" style="top:0;">
    <li style="top:141px;">Immediate availability</li>
    <li style="top:167px;">Efficient logistics</li>
    <li style="top:191px;">Stock optimization</li>
  </ul>

  <h3 class="abs sub-head" style="top:207px;">Training</h3>
  <p class="abs body-copy sub-copy" style="top:227px;">Training is a part of the project, allowing for improved efficiency and cost savings during production. Line stoppages, be they for minutes or for hours,are&nbsp; often simply due to elementary issues or to inadequate operator training.</p>
  <p class="abs body-copy sub-copy" style="top:292px;">Nortec dedicates time and energy to preparing training for customer personnel, to familiarize operators with the line and ensure safe and efficient line management and operation.</p>

  <h3 class="abs sub-head" style="top:337px;">Maintenance Programs</h3>
  <p class="abs body-copy sub-copy" style="top:355px;">We provide full preventive maintenance programs, based on specific customer needs and requirements and on the type of line installed. We offer annual contracts or multi-year maintenance.</p>

  <div class="abs contact contact-left">
    <div class="brand"><i></i>Nortec Group</div>
    <p class="name">Nortec Packaging Systems s.r.l.</p>
    <p class="line">Via delle Rose, 8 – 20100 Milano</p>
    <p class="line">P.IVA/CF: 01234567890</p>
    <p class="line phone"><b>Phone:</b> +39 0200 000000</p>
    <p class="line email"><b>Email:</b> info@nortec.example</p>
  </div>
  <div class="abs divider"></div>
  <div class="abs contact contact-right">
    <div class="brand"><i></i>Nortec Group</div>
    <p class="name">Nortec Polska s.c.</p>
    <p class="line">Polna 7- 00-000 Radom</p>
    <p class="line">&nbsp;</p>
    <p class="line phone"><b>Phone:</b> 000 000 0000</p>
    <p class="line email"><b>Email:</b> biuro@nortec.example</p>
  </div>
  <p class="abs web">www.nortec.example</p>

  <!-- Cover -->
  <div class="abs cover-photo" role="img" aria-label="Photograph of a stainless steel bottle filling machine with green glass bottles"></div>
  <div class="abs cover-badge"><i></i><span>Nortec Group</span></div>

</main>
</body>
</html>
```